Dorvelan Swimming & Athletics Center

We need Business Card for a Athletics center
The logo frome the Uploaded Files ( b card fimal)
Οn one side of card we need the logo of company the Contact and the website:
1. Address:(Limassol, Cyprus 12-14 Stavrinelou str,Ano Trimeni,P.C. 4832)

2.Phone number: (+357) 25-704263

3. Mail: info@dorvelanfit.example

3. Website: www.dorvelanfit.example

Οn the other side of the card we need to write the sport of the company:

1. Artistic Gymnastics
2. Swimming
3. Gym - Fitness
4. Programs
5. Dancing
5.Tennis

From the Uploaded Files you can get the logo.In a logo is behind the black color which can be removed from logo.

Υou can use that color you want.
.
Updates

Industry/Entity Type

Business

Font styles to use
Decorative

Colors
0555a3
ffcf3e
3176b5
0692cd
add136
f04a50
000000
cfcfcf
9d9d9d

Requirements
Should not have
• photos with faces
• photo fro the Website:www.dorvelanfit.example

```html
<!DOCTYPE html>
<html lang="en">
<head>
<meta charset="utf-8">
<title>Dorvelan Swimming &amp; Athletics Center — Business Card</title>
<link href="https://fonts.googleapis.com/css2?family=Montserrat:wght@400;500;700;800&display=swap" rel="stylesheet">
<style>
  :root {
    --stage: #2b2b2b;
    --card: #050505;
    --gold: #f7b51c;
    --yellow: #ffcf3e;
    --lime: #add136;
    --white: #f2f2f2;
    --grey: #9d9d9d;
    --rule: #5a5a5a;
  }
  * { margin: 0; padding: 0; box-sizing: border-box; }
  html, body { width: 1200px; height: 900px; overflow: hidden; }
  body {
    background: var(--stage);
    font-family: "Montserrat", sans-serif;
    color: var(--white);
    position: relative;
  }
  .card {
    position: absolute;
    width: 620px;
    height: 354px;
    background: var(--card);
    border-radius: 22px;
    box-shadow: 0 14px 30px rgba(0,0,0,0.55);
    overflow: hidden;
  }
  .card--front { left: 150px; top: 60px; }
  .card--back { left: 430px; top: 486px; }

  /* Front */
  .brand-name {
    position: absolute;
    left: 46px; top: 110px;
    font-size: 72px;
    font-weight: 800;
    letter-spacing: 2px;
    color: var(--gold);
    line-height: 1;
  }
  .brand-mark {
    position: absolute;
    left: 500px; top: 96px;
    width: 84px; height: 84px;
    border-radius: 50%;
    border: 3px solid var(--gold);
  }
  .sports-list {
    position: absolute;
    left: 62px; top: 196px;
    list-style: none;
  }
  .sports-list li {
    font-size: 15px;
    font-weight: 500;
    letter-spacing: 0.5px;
    line-height: 21px;
    text-transform: uppercase;
    position: relative;
    padding-left: 20px;
  }
  .sports-list li::before {
    content: "";
    position: absolute;
    left: 0; top: 7px;
    width: 8px; height: 8px;
    border-radius: 50%;
    background: var(--yellow);
  }
  .front-web {
    position: absolute;
    right: 40px; top: 196px;
    font-size: 18px;
    font-weight: 500;
  }
  .front-web b, .contact-web b { color: var(--yellow); font-weight: 700; }

  /* Back */
  .back-mark {
    position: absolute;
    left: 60px; top: 70px;
    width: 200px; height: 200px;
    border-radius: 50%;
    border: 6px solid var(--gold);
    display: flex; align-items: center; justify-content: center;
  }
  .back-mark span {
    font-size: 26px;
    font-weight: 800;
    letter-spacing: 1px;
    color: var(--gold);
  }
  .divider {
    position: absolute;
    left: 318px; top: 60px;
    width: 1px; height: 240px;
    background: linear-gradient(to bottom, transparent, var(--rule), transparent);
  }
  .contact {
    position: absolute;
    left: 342px; top: 62px;
    width: 260px;
  }
  .contact-name {
    font-size: 26px;
    font-weight: 700;
    color: var(--lime);
    line-height: 1.1;
  }
  .contact-role {
    font-size: 14px;
    margin: 4px 0 12px 18px;
  }
  .contact-address {
    font-size: 14px;
    line-height: 19px;
    margin: 0 0 10px 18px;
  }
  .contact-lines { list-style: none; margin-left: 18px; }
  .contact-lines li {
    font-size: 14px;
    line-height: 21px;
    display: flex; align-items: center; gap: 8px;
  }
  .contact-lines svg { width: 12px; height: 12px; flex: none; }
</style>
</head>
<body>

<section class="card card--front">
  <div class="brand-name">DORVELAN</div>
  <div class="brand-mark"></div>
  <ul class="sports-list">
    <li>Artistic Gymnastics</li>
    <li>Swimming</li>
    <li>Gym - Fitness</li>
    <li>Programs</li>
    <li>Dancing</li>
    <li>Tennis</li>
  </ul>
  <div class="front-web">www.<b>dorvelanfit</b>.example</div>
</section>

<section class="card card--back">
  <div class="back-mark"><span>DORVELAN</span></div>
  <div class="divider"></div>
  <div class="contact">
    <div class="contact-name">Marek Halloran</div>
    <div class="contact-role">Director</div>
    <div class="contact-address">Limassol, Cyprus<br>12-14 Stavrinelou<br>str,Ano Trimeni,P.C. 4832</div>
    <ul class="contact-lines">
      <li>
        <svg viewBox="0 0 12 12" aria-hidden="true"><path d="M2.5 1 L4.5 1 L5.3 3.6 L4 4.6 Q5 7 7.4 8 L8.4 6.7 L11 7.5 L11 9.5 Q10.5 11 9 11 Q1 10 1 2.8 Q1 1.3 2.5 1 Z" fill="var(--lime)"/></svg>
        (+357) 25-704263
      </li>
      <li>
        <svg viewBox="0 0 12 12" aria-hidden="true"><rect x="1" y="2.5" width="10" height="7" fill="none" stroke="var(--lime)" stroke-width="1.3"/><path d="M1 2.5 L6 6.5 L11 2.5" fill="none" stroke="var(--lime)" stroke-width="1.3"/></svg>
        info@dorvelanfit.example
      </li>
      <li class="contact-web">
        <svg viewBox="0 0 12 12" aria-hidden="true"><circle cx="6" cy="6" r="5" fill="none" stroke="var(--lime)" stroke-width="1.2"/><ellipse cx="6" cy="6" rx="2.2" ry="5" fill="none" stroke="var(--lime)" stroke-width="1"/><path d="M1 6 H11" stroke="var(--lime)" stroke-width="1"/></svg>
        <span>www.<b style="color:var(--lime)">dorvelanfit</b>.example</span>
      </li>
    </ul>
  </div>
</section>

</body>
</html>
```